RTB sticker for the back window of a car

Well this design is for the back of our car. We want it to be plain and simple but stand out. I have put something together which is a bit to plain and i would like to to look a little bit different. Possibly have a picture of a shipping container on it so people know what we are trying to sell? I don't need our logo on there but i want the phone number and email. Thank you in advance.

Requirements
Must have
• The phone number 0462 517 093 not the one in the picture please.
• Also must have the email that IS in the picture please.
Nice to have
• A picture of a shipping container so people know what we are talking about.

```html
<!DOCTYPE html>
<html lang="en">
<head>
<meta charset="utf-8">
<title>Rear Window Sticker</title>
<link href="https://fonts.googleapis.com/css2?family=Roboto+Condensed:wght@700&display=swap" rel="stylesheet">
<style>
  :root {
    --crimson: #b31b2e;
    --crimson-dark: #8a1120;
    --white: #ffffff;
    --sand: #e4ddd1;
    --ink: #111111;
    --page: #f1f1f1;
  }
  html, body {
    margin: 0;
    padding: 0;
    width: 1200px;
    height: 999px;
    overflow: hidden;
    background: var(--page);
  }
  .sticker {
    position: absolute;
    left: 50px;
    top: 302px;
    width: 1100px;
    height: 395px;
    border-radius: 44px;
    overflow: hidden;
    background: var(--white);
    font-family: "Roboto Condensed", "Arial Narrow", sans-serif;
    font-weight: 700;
  }
  .top-band {
    position: absolute;
    left: 0;
    top: 0;
    width: 100%;
    height: 34px;
    background: var(--crimson-dark);
  }
  .backdrop-crimson {
    position: absolute;
    left: 0;
    bottom: 0;
    width: 560px;
    height: 110px;
    background: linear-gradient(180deg, rgba(179, 27, 46, 0) 0%, var(--crimson) 55%, var(--crimson-dark) 100%);
  }
  .backdrop-sand {
    position: absolute;
    right: 0;
    bottom: 0;
    width: 540px;
    height: 110px;
    background: linear-gradient(180deg, rgba(228, 221, 209, 0) 0%, var(--sand) 70%);
  }
  .headline {
    position: absolute;
    left: 122px;
    top: 86px;
    margin: 0;
    color: var(--crimson);
    font-size: 74px;
    line-height: 72px;
    letter-spacing: -1px;
  }
  .headline span { display: block; }
  .container-art {
    position: absolute;
    left: 462px;
    top: 100px;
    width: 200px;
    height: 96px;
    background: linear-gradient(90deg, var(--crimson-dark), var(--crimson));
  }
  .offer {
    position: absolute;
    left: 684px;
    top: 96px;
    margin: 0;
    color: var(--crimson);
    white-space: nowrap;
    letter-spacing: -1px;
  }
  .offer-for { font-size: 48px; }
  .offer-sale { font-size: 106px; }
  .contact {
    position: absolute;
    left: 584px;
    top: 226px;
    color: var(--ink);
  }
  .contact-phone {
    margin: 0;
    font-size: 48px;
    line-height: 56px;
  }
  .contact-email {
    margin: 6px 0 0;
    font-size: 29px;
    line-height: 34px;
  }
</style>
</head>
<body>
  <div class="sticker">
    <div class="top-band"></div>
    <div class="backdrop-crimson" role="img" aria-label="Crimson wave decoration"></div>
    <div class="backdrop-sand" role="img" aria-label="Sand swirl decoration"></div>

    <h1 class="headline"><span>Shipping</span><span>Containers</span></h1>

    <div class="container-art" role="img" aria-label="Shipping container illustration"></div>

    <p class="offer"><span class="offer-for">for</span><span class="offer-sale">Sale</span></p>

    <div class="contact">
      <p class="contact-phone">Ph: 0462 517 093</p>
      <p class="contact-email">Email: sales@example.com</p>
    </div>
  </div>
</body>
</html>
```